Pharmacy handmade, Personalized Medical Cosmetics Label

Medical Cosmetics label, elegant and professional looking. The creams are Dermatologist formulated and are prepared by local Pharmacy. The label should be versatile and allow space for hand writing to be filled by the pharmacist preparing the product.
The following information will be handwritten:
Upper lid - Lid Balm No.5 ; Marigold, Retinol ; 30
Lower Bottom - Teodora Halvik ; Signature ; 01.01.2017
Upper Lid Label
Velluto Skin (logo)
Doctor Series
(circular pattern - Doctor Formulated, Registered Pharmacy, Handmade, Highest Medical Standards)
(Lid Balm No.5 - in hand writing and different color, maybe red)
Key Ingredients: (Marigold, Retinol - in hand writing, same color as above, maybe red)
(box with hand writing 30) ml
Lower Bottom Label (underneath surface of the container)
Made for Velluto Skin by
Pharmacy Lorant, 7 Pelister blvd., Sofia, ph. 0893517460
Patient: (Teodora Halvik- in hand writing)
Pharmacist: (Signature - in hand writing)
Date: (01.01.2017 - in hand writing)
For External Use
good for 60 days after preparation
Ingredients: Retinol, Marigold Extract, Water, Glycerin, Stearyl Alcohol, Wheat Germ Oil, Polysorbate 60, Sesame Oil, Myristyl Myristate, Cetyl Alcohol, Sorbitan Stearate, Phenoxyethanol, Calendula Extract, Cornflower Extract, Sodium Alginate, Sodium Citrate.
The container lid and bottom are 5 cm = 50 mm in diameter. Made from aluminum and contain 30ml or 50ml.
Please refer to the screen shots from my Web Site to get the feeling for the color pallet and professional look. These creams will be sold on this website. They are custom made by a registered Pharmacy right on the spot after the order has been placed. This is why I need more space for the hand written notes made by the pharmacist who prepared the order.
Please make the design professional, simple and serious colors, like light brown, beige, black or dark brown letters, red hand writing (will be filled by pen or thin marker by the Pharmacist by hand, depending on the order, patient name, etc.)
Thank you.
female 24 - 49 year old
Medical

```html
<!DOCTYPE html>
<html lang="en">
<head>
<meta charset="utf-8">
<title>Velluto Skin – Lid Balm No.5 Lid Label</title>
<link rel="stylesheet" href="https://fonts.googleapis.com/css2?family=Quicksand:wght@400;500&family=Courgette&display=swap">
<style>
  :root {
    --paper: #ffffff;
    --taupe: #a08f83;
    --taupe-dark: #7d6c60;
    --rim: #8a7a6e;
    --ink-red: #8e2a22;
    --cream: #fdfbf8;
  }
  html, body {
    margin: 0;
    padding: 0;
    width: 1200px;
    height: 1200px;
    overflow: hidden;
    background: var(--paper);
  }
  .lid-label {
    display: block;
    width: 1200px;
    height: 1200px;
  }
  .label-edge { fill: var(--paper); stroke: var(--rim); stroke-width: 2; }
  .ring-text {
    font-family: "Quicksand", sans-serif;
    font-weight: 400;
    font-size: 46px;
    letter-spacing: 2px;
    fill: var(--taupe-dark);
  }
  .ring-dot { fill: var(--taupe-dark); }
  .centre-disc { fill: var(--taupe); }
  .centre-rim {
    fill: none;
    stroke: var(--rim);
    stroke-width: 5;
    stroke-linecap: round;
    stroke-dasharray: 0 9;
  }
  .brand-name {
    font-family: "Quicksand", sans-serif;
    font-weight: 500;
    font-size: 84px;
    fill: var(--cream);
    letter-spacing: 1px;
  }
  .name-band { fill: var(--paper); }
  .product-name {
    font-family: "Courgette", cursive;
    font-size: 58px;
    fill: var(--ink-red);
  }
  .ingredients-line {
    font-family: "Courgette", cursive;
    font-size: 38px;
    fill: var(--ink-red);
  }
  .volume {
    font-family: "Courgette", cursive;
    font-size: 28px;
    fill: var(--cream);
  }
</style>
</head>
<body>
<svg class="lid-label" viewBox="0 0 1200 1200" xmlns="http://www.w3.org/2000/svg">
  <defs>
    <path id="ring-path" d="M 70,600 A 530 530 0 1 1 1130,600 A 530 530 0 1 1 70,600"/>
    <clipPath id="disc-clip">
      <circle cx="600" cy="600" r="500"/>
    </clipPath>
  </defs>

  <circle class="label-edge" cx="600" cy="600" r="592"/>

  <g class="ring-words">
    <text class="ring-text" text-anchor="middle"><textPath href="#ring-path" startOffset="7%">Doctor Formulated</textPath></text>
    <text class="ring-text" text-anchor="middle"><textPath href="#ring-path" startOffset="25%">Handmade</textPath></text>
    <text class="ring-text" text-anchor="middle"><textPath href="#ring-path" startOffset="51%">Highest Medical Standards</textPath></text>
    <text class="ring-text" text-anchor="middle"><textPath href="#ring-path" startOffset="76%">Registered Pharmacy</textPath></text>
  </g>

  <g class="ring-dots">
    <circle class="ring-dot" cx="345" cy="126" r="6"/>
    <circle class="ring-dot" cx="893" cy="152" r="6"/>
    <circle class="ring-dot" cx="884" cy="1046" r="6"/>
    <circle class="ring-dot" cx="112" cy="833" r="6"/>
  </g>

  <circle class="centre-disc" cx="600" cy="600" r="500"/>
  <rect class="name-band" x="90" y="533" width="1020" height="128" clip-path="url(#disc-clip)"/>
  <circle class="centre-rim" cx="600" cy="600" r="502"/>

  <text class="brand-name" x="600" y="420" text-anchor="middle">Velluto Skin</text>
  <text class="product-name" x="600" y="620" text-anchor="middle">Lid Balm No.5</text>
  <text class="ingredients-line" x="600" y="752" text-anchor="middle">Key Ingredients: Retinol, Marigold</text>
  <text class="volume" x="600" y="1053" text-anchor="middle">30ml</text>
</svg>
</body>
</html>
```